Harbor Zentrik needs a new Website Design

We need a WEB site landing page (/template) design, we currently have a company logo.We like the Valtor.com web designEnclosed is our company logo.Our Current website is https://www.harborzentrik.com.au/

1 page

```html
<!DOCTYPE html>
<html lang="en">
<head>
<meta charset="utf-8">
<title>Harbor Zentrik – White-Label Communications</title>
<link rel="stylesheet" href="https://fonts.googleapis.com/css2?family=Roboto+Condensed:wght@400;700&family=Roboto:wght@400;500;700&display=swap">
<style>
:root{
  --blue:#1747d6;
  --blue-bright:#1f5ae6;
  --ink:#17183a;
  --text:#4a4b63;
  --muted:#8a8ca3;
  --grey-bg:#f2f2f5;
  --lavender:#eceefb;
  --mint:#c9f7e3;
  --white:#ffffff;
  --green:#5cb85c;
}
*{box-sizing:border-box;margin:0;padding:0}
html,body{width:1200px;height:4800px;overflow:hidden;background:var(--white)}
body{font-family:"Roboto",sans-serif;color:var(--ink);position:relative}
.abs{position:absolute}
h1,h2,h3{font-family:"Roboto Condensed",sans-serif;font-weight:700;line-height:1.15}
.accent{color:var(--blue)}
.btn{position:absolute;display:flex;align-items:center;justify-content:center;font-weight:700;font-size:14px;border-radius:24px;background:var(--blue);color:var(--white);width:158px;height:45px}
.btn-outline{background:var(--white);color:var(--ink);border:2px solid var(--blue);border-radius:8px;width:186px;height:52px;font-size:15px}
.underline{position:absolute;height:4px;width:50px;background:var(--blue);border-radius:2px}
.para{position:absolute;font-size:12.5px;line-height:25px;color:var(--text)}
.feature-title{position:absolute;font-size:37px}
.feature-sub{position:absolute;font-size:18px;color:var(--ink)}
.bullets{position:absolute;list-style:none;font-size:12.5px;font-weight:500;color:var(--ink)}
.bullets li{height:25px}
.bullets li::before{content:"• "}

/* header */
.site-header{position:absolute;top:0;left:0;width:1200px;height:93px;border-bottom:1px solid #ececf2;background:var(--white)}
.brand{position:absolute;display:flex;align-items:center;gap:8px;font-family:"Roboto",sans-serif;font-weight:700;letter-spacing:1px}
.brand-dot{width:24px;height:24px;border-radius:50%}
.nav{position:absolute;left:445px;top:37px;display:flex;gap:24px;font-size:12.5px;font-weight:500;color:var(--ink)}

/* hero */
.hero-title{left:166px;top:218px;font-size:38px;color:var(--ink)}
.hero-sub{left:166px;top:368px;font-size:19px;color:var(--text);line-height:24px}

/* components */
.components{position:absolute;top:618px;left:0;width:1200px;height:977px;background:var(--grey-bg)}
.card{position:absolute;width:235px;height:237px;background:var(--white);box-shadow:0 4px 14px rgba(20,30,80,.08)}
.card-icon{position:absolute;left:58px;top:28px;width:118px;height:118px;border-radius:50%;background:linear-gradient(135deg,#e4e6ee,#cfd8f5)}
.card-label{position:absolute;left:0;width:100%;top:190px;text-align:center;font-size:13px;font-weight:700;color:var(--ink)}

/* pbx dashboard */
.pbx-shot{position:absolute;left:66px;top:1712px;width:474px;height:298px}
.sidebar{position:absolute;left:2px;top:48px;width:120px;height:250px;background:linear-gradient(#3fb6ee,#2aa4e6);color:var(--white);font-size:7px;padding:20px 8px;line-height:12.3px;font-weight:700}

.lavender-band{position:absolute;left:0;top:2090px;width:1200px;height:650px;background:var(--lavender);clip-path:polygon(0 85px,1200px 0,1200px 650px,0 650px)}

.site-footer{position:absolute;left:0;top:4490px;width:1200px;height:310px;background:var(--blue);color:var(--white)}
.footer-col{position:absolute;text-align:center;font-size:10px;line-height:17px}
.footer-col h4{font-size:14px;font-weight:400;margin-bottom:12px}
.footer-nav{position:absolute;left:345px;top:70px;font-size:10px}
.footer-nav h4{font-size:14px;font-weight:400;margin-bottom:14px}
.footer-nav li{list-style:none;height:25.5px}
</style>
</head>
<body>

<header class="site-header">
  <div class="brand" style="left:170px;top:32px;color:var(--blue);font-size:17px">
    <span class="brand-dot" style="background:var(--blue-bright)"></span>HARBOR ZENTRIK
  </div>
  <nav class="nav">
    <span>Home</span><span>Voice ▾</span><span>Data</span><span>Hardware ▾</span><span>Services Request ▾</span><span>Terms &amp; Conditions ▾</span><span>Status</span>
    <svg width="12" height="12" viewBox="0 0 12 12" style="margin-top:2px"><circle cx="5" cy="5" r="3.6" fill="none" stroke="#17183a" stroke-width="1.5"/><line x1="7.6" y1="7.6" x2="11" y2="11" stroke="#17183a" stroke-width="1.5"/></svg>
  </nav>
</header>

<section class="hero">
  <h1 class="abs hero-title">White-Label <span class="accent">Solution</span><br>for all your<br><span class="accent">Communication</span> Needs</h1>
  <p class="abs hero-sub">Liberating Businesses from Traditional<br>Communications Systems</p>
  <a class="btn btn-outline" style="left:166px;top:460px">Get Started</a>
  <div class="abs" role="img" aria-label="Illustration of two people working with floating interface panels" style="left:655px;top:190px;width:420px;height:330px;border-radius:48% 52% 45% 55%;background:linear-gradient(135deg,#eef0fc,#dfe3f9)"></div>
</section>

<section class="components">
  <p class="abs" style="left:0;width:1200px;top:95px;text-align:center;font-size:22px;font-weight:500">We have all the <span class="accent">components</span> to</p>
  <h2 class="abs" style="left:0;width:1200px;top:130px;text-align:center;font-size:40px">start and run your own <span class="accent">White Label Telco</span></h2>
  <div class="abs" style="left:490px;top:198px;width:220px;height:5px;background:#d7dae6"></div>
  <div class="abs" style="left:490px;top:198px;width:92px;height:5px;background:var(--blue)"></div>

  <div class="card" style="left:185px;top:303px"><div class="card-icon" role="img" aria-label="Payment card icon"></div><div class="card-label">Invoice &amp; Payment Platform</div></div>
  <div class="card" style="left:482px;top:303px"><div class="card-icon" role="img" aria-label="Video call and chat icon"></div><div class="card-label">Unified Communications</div></div>
  <div class="card" style="left:779px;top:303px"><div class="card-icon" role="img" aria-label="Cloud network icon"></div><div class="card-label">Cloud IP PBX</div></div>
  <div class="card" style="left:185px;top:604px"><div class="card-icon" role="img" aria-label="Circuit board icon"></div><div class="card-label">Data Services</div></div>
  <div class="card" style="left:482px;top:604px"><div class="card-icon" role="img" aria-label="Lifebuoy support icon"></div><div class="card-label">Support</div></div>
  <div class="card" style="left:779px;top:604px"><div class="card-icon" role="img" aria-label="Phone handset icon"></div><div class="card-label">Voice Services</div></div>
</section>

<section class="pbx">
  <div class="pbx-shot">
    <div class="abs" style="left:6px;top:0;font-size:18px;color:#3fb6ee;font-weight:500">Zentrik UC</div>
    <div class="abs" style="left:140px;top:6px;width:334px;height:18px;border-bottom:1px solid #e5e5e5;font-size:8px;color:var(--muted)">200 · ZentrikPBX</div>
    <div class="sidebar">Dashboard<br>Extensions<br>DIDs<br>Conferences<br>IVR<br>Queues<br>Voicemail<br>Monitor<br>Reports<br>Statistics<br>PBX<br>System<br>LCR<br>Apps</div>
    <div class="abs" style="left:140px;top:80px;font-size:30px;color:#c9c9cf">System Dashboard</div>
    <div class="abs" style="left:134px;top:135px;width:160px;height:160px;background:#f3f3f5;font-size:13px;color:#777;padding:8px">Total calls
      <div style="text-align:right;padding-right:50px;margin-top:16px;line-height:22px">Now <b>1</b><br>Last Hour <b>1</b><br>Today <b>7</b></div></div>
    <div class="abs" style="left:310px;top:135px;width:164px;height:160px;background:#f3f3f5;font-size:13px;color:#777;padding:8px">Answered calls
      <svg class="abs" style="left:32px;top:32px" width="100" height="100" viewBox="0 0 100 100"><circle cx="50" cy="50" r="42" fill="none" stroke="#e2e2e2" stroke-width="12"/><circle cx="50" cy="50" r="42" fill="none" stroke="#38a812" stroke-width="12" stroke-dasharray="240 264" transform="rotate(-90 50 50)"/><text x="50" y="54" font-size="11" text-anchor="middle" fill="#777">5</text></svg></div>
  </div>
  <h2 class="feature-title" style="left:633px;top:1700px">Cloud <span class="accent">IP PBX</span></h2>
  <p class="feature-sub" style="left:633px;top:1753px">Multiple IP PBXs on a single instance</p>
  <div class="underline" style="left:633px;top:1785px"></div>
  <p class="para" style="left:633px;top:1815px;width:360px">A Multi-Tenant ZentrikPBX is able to handle multiple customers (tenants) with a single instance of the software. Even though every customer has a dedicated PBX, they all share the same core engine instance. Using the single instance.</p>
  <a class="btn" style="left:633px;top:1955px">Learn More</a>
  <svg class="abs" style="left:1055px;top:2020px" width="145" height="150">
    <defs><pattern id="dot-grid" width="17" height="17" patternUnits="userSpaceOnUse"><circle cx="3" cy="3" r="2" fill="#8a8ca3"/></pattern></defs>
    <rect width="145" height="150" fill="url(#dot-grid)"/>
  </svg>
</section>

<div class="lavender-band"></div>
<section class="unified">
  <h2 class="feature-title" style="left:174px;top:2296px">Unified <span class="accent">Communications</span></h2>
  <p class="feature-sub" style="left:174px;top:2350px">Available on Desktop &amp; Mobile</p>
  <div class="underline" style="left:174px;top:2381px"></div>
  <p class="para" style="left:174px;top:2415px;width:370px">Communicator is a Desktop &amp; Mobile Unified Communications application designed to provide business users with a set of features and benefits capable of transforming your company communications system into a real powerhouse.</p>
  <p class="para" style="left:174px;top:2540px;width:370px">It is available on all major desktop systems, and on the leading phone and tablet platforms as a mobile application.</p>
  <a class="btn" style="left:174px;top:2645px">Learn More</a>
  <div class="abs" style="left:688px;top:2298px;width:470px;height:325px;background:var(--white);box-shadow:0 2px 10px rgba(0,0,0,.08)">
    <div class="abs" style="left:6px;top:10px;width:158px;height:300px;border:1px solid #ddd"><div style="background:#2d8be0;color:#fff;font-size:8px;padding:4px">Voicemail</div></div>
    <div class="abs" style="left:172px;top:10px;width:120px;height:300px;border:1px solid #ddd"><div style="background:#2d8be0;color:#fff;font-size:8px;padding:4px">Phone</div>
      <svg width="118" height="200"><circle cx="59" cy="130" r="9" fill="#3cbf4a"/><rect x="20" y="250" width="0" height="0"/></svg></div>
    <div class="abs" style="left:298px;top:10px;width:164px;height:300px;border:1px solid #ddd"><div style="background:#2d8be0;color:#fff;font-size:8px;padding:4px;margin-top:30px">Contacts</div></div>
  </div>
</section>

<section class="invoice">
  <div class="abs" style="left:1060px;top:2820px;width:220px;height:420px;border-radius:50% 0 0 50%;background:var(--lavender)"></div>
  <div class="abs" style="left:33px;top:2870px;width:472px;height:260px;border:1px solid #e6e6ea;background:var(--white)">
    <div class="abs" style="left:0;top:0;width:110px;height:260px;background:#f5f5f7;border-right:1px solid #e6e6ea"></div>
    <div class="abs" style="left:118px;top:4px;font-size:7px;color:var(--muted)">Dashboard</div>
    <div class="abs" style="left:128px;top:60px;width:162px;height:42px;background:#4cba5e;color:#fff;font-size:18px;text-align:right;padding:4px 8px">14<div style="font-size:6px">Active Customers</div></div>
    <div class="abs" style="left:300px;top:60px;width:162px;height:42px;background:#3b7fd6;color:#fff;font-size:18px;text-align:right;padding:4px 8px">34<div style="font-size:6px">Total Customers</div></div>
    <div class="abs" style="left:128px;top:125px;width:334px;height:130px;border:1px solid #eee"></div>
  </div>
  <h2 class="feature-title" style="left:600px;top:2862px"><span class="accent">Invoice &amp;</span> Payment Platform</h2>
  <p class="feature-sub" style="left:600px;top:2915px">All pieces in one for an assertive management</p>
  <p class="para" style="left:603px;top:2992px;width:370px">Access Portal is a fully-featured telecom customer portal, designed for integration with one or many ZentrikPBX telephony switches. Access Portal has a friendly GUI that enables efficient, automated billing, invoicing and payments, allowing you to spend less time dealing with the administration of your company and more time to SELL!</p>
  <a class="btn" style="left:603px;top:3165px">Learn More</a>
</section>

<section class="data">
  <div class="abs" style="left:-130px;top:3260px;width:260px;height:250px;border-radius:50%;background:var(--mint)"></div>
  <h2 class="feature-title" style="left:178px;top:3442px"><span class="accent">Data</span> Services</h2>
  <p class="feature-sub" style="left:178px;top:3496px">Data Networks * not all services available all areas</p>
  <ul class="bullets" style="left:178px;top:3565px">
    <li>Access to the Regional Broadband Grid</li><li>Fibre Network Access</li><li>Ethernet Over Copper Access</li><li>Fixed Wireless</li>
  </ul>
  <a class="btn" style="left:178px;top:3690px">Learn More</a>
  <div class="abs" role="img" aria-label="World map with connected network points" style="left:655px;top:3460px;width:560px;height:340px;border-radius:50%;background:linear-gradient(135deg,#eceef2,#dcdfe8)"></div>
</section>

<section class="voice">
  <div class="abs" style="left:-40px;top:3990px;width:390px;height:500px;border-radius:0 50% 50% 0;background:var(--lavender)"></div>
  <div class="abs" role="img" aria-label="Illustration of a person with a headset seated on a chair" style="left:50px;top:4040px;width:300px;height:390px;border-radius:45%;background:linear-gradient(#dfe2f6,#c9cdea)"></div>
  <div class="abs" role="img" aria-label="Chat bubbles on a dark circle" style="left:335px;top:3955px;width:250px;height:250px;border-radius:50%;background:#2f2e41"></div>
  <h2 class="feature-title" style="left:695px;top:4007px"><span class="accent">Voice</span> Services</h2>
  <p class="feature-sub" style="left:695px;top:4061px">Everything for your Business Communications</p>
  <ul class="bullets" style="left:700px;top:4133px">
    <li style="height:35px">Inbound Services, Call Termination, 1300 &amp; 1800 Services</li>
    <li style="height:35px">Phone  Number, Number Porting, Virtual Fax</li>
    <li>Sip Trunk and Connectivity, SMS, Conference Bridge</li>
  </ul>
  <a class="btn" style="left:695px;top:4250px">Learn More</a>
</section>

<footer class="site-footer">
  <div class="brand" style="left:45px;top:85px;color:var(--white);font-size:26px">
    <span class="brand-dot" style="background:var(--white);width:34px;height:34px"></span>HARBOR ZENTRIK
  </div>
  <p class="abs" style="left:50px;top:168px;font-size:10px">ABN: 48 902 115 367</p>
  <p class="abs" style="left:50px;top:200px;font-size:10px">PO Box 1187, Fyshwick ACT 2609</p>
  <div class="footer-nav"><h4>Navigation</h4><ul><li>Home</li><li>Voice</li><li>Data</li><li>Hardware</li><li>Services Request</li><li>Terms &amp; Conditions</li><li>Status</li></ul></div>
  <div class="footer-col" style="left:508px;top:70px;width:160px"><h4>Administration</h4>admin@harborzentrik.com.au<br>+61 2 6100 4420</div>
  <div class="footer-col" style="left:710px;top:70px;width:160px"><h4>Accounts</h4>accounts@harborzentrik.com.au<br>+61 2 6100 4420</div>
  <div class="footer-col" style="left:913px;top:60px;width:200px"><h4>Support</h4>Our technical support team is always available to you via phone, live chat and support ticketing system.</div>
  <p class="abs" style="left:928px;top:255px;font-size:10px">Copyright © 2019, All Right Reserved</p>
</footer>

</body>
</html>
```